One page company profile for exclusive wine import

Valtrenor is an importer of exclusive, rare wines into indonesia. We would like a stylish, classy, upmarket but professional one pager containing our company profile.

Please include the text we prepared (see must haves) and read through it to get a better understanding of what our company is doing

We would like the one pager to have a dark background, and contain a drawing or drawing-style picture related to wine and/or global import (see examples). We would like to have it in PDF as well as in a word-template so we can later produce translations and/or adaptations to the text.

Target Market(s)

The one pagers is directed to distributors and upmarket hotels and restaurants.

Requirements
Must have
• We would like the one pager to have a dark background, and contain a drawing or drawing-style picture related to wine and/or global import (see examples)
• Our logo (see files) on the one pager
• The following contact details: E-mail: info@valtrenor-example.eu
• Word template and PDF
• The following text:
• "Valtrenor brings rare, exceptional wines to the Indonesian market. We
• specialize in French and Italian wines that even in Europe are very hard
• to get by. We have an extensive network of big and small, famous and less
• known winemakers that reserve a portion of their production for us.
• Together with them, we supply the market with an excellent range of the
• absolute best European wines.
• We buy our products directly at the winemaker in France or Italy Through a
• licensed importer, the wines are brought to Indonesia by airfreight and
• stored in air-conditioned, optimal conditions, awaiting distribution to
• our customers. All of this ensured that the wine loses none of its quality
• during transport from the winemaker to the customer.
• We always look out for partners that are eager to distribute or retail.
• Our intentions working with them are always to work on a long term basis.
• With these intentions we see that both sides together have to engage
• themselves to succeed in sales and establishing brand recognition in the
• Indonesian market. Our philosophy is based on trust, responsibility,
• mutual respect and of course a love for great wine!
• We advise our clients on tasting, food pairing, storing and aging the wine
• and provide a technical datasheet with all our bottles. We pride ourselves
• in our customer service and are always available for any enquiry."
Should not have
• clichés like pictures of grapes, vineyards, barrels, etc... (stylised drawings are preferred and allowed)

```html
<!DOCTYPE html>
<html lang="en">
<head>
<meta charset="utf-8">
<title>Valtrenor – Company Profile</title>
<link rel="stylesheet" href="https://fonts.googleapis.com/css2?family=Raleway:wght@400;700&display=swap">
<style>
  :root {
    --wine-deep: #3a0a12;
    --wine-mid: #6e1420;
    --wine-bright: #8c1c2a;
    --band: #4a0c14;
    --line: rgba(255,255,255,0.85);
    --text: #f4e9ea;
    --glass-light: #c9a9ac;
    --glass-wine: #8a0f18;
  }
  html, body {
    margin: 0;
    padding: 0;
    width: 936px;
    height: 1200px;
    overflow: hidden;
    background: var(--wine-deep);
  }
  .profile-page {
    position: relative;
    width: 936px;
    height: 1200px;
    overflow: hidden;
    font-family: "Raleway", sans-serif;
    color: var(--text);
    background:
      radial-gradient(ellipse 70% 60% at 60% 60%, var(--wine-bright) 0%, var(--wine-mid) 45%, var(--wine-deep) 100%);
  }
  .profile-page::before {
    content: "";
    position: absolute;
    left: 0; top: 0; bottom: 0;
    width: 60px;
    background: linear-gradient(90deg, rgba(20,2,6,0.55), rgba(20,2,6,0));
  }
  .facet-lines {
    position: absolute;
    inset: 0;
  }
  .content-frame {
    position: absolute;
    left: 47px;
    top: 0;
    width: 549px;
    height: 1002px;
    border: 1px solid var(--line);
    border-top: none;
    box-sizing: border-box;
  }
  .brand {
    position: absolute;
    left: 51px;
    top: 58px;
    display: flex;
    align-items: center;
    gap: 18px;
  }
  .brand-dot {
    width: 78px;
    height: 78px;
    border-radius: 50%;
    background: var(--text);
  }
  .brand-name {
    font-weight: 700;
    font-size: 42px;
    letter-spacing: 1px;
    color: var(--text);
    text-transform: uppercase;
  }
  .company-text {
    position: absolute;
    left: 83px;
    top: 332px;
    width: 478px;
    margin: 0;
    font-size: 16.4px;
    line-height: 22.3px;
    text-align: justify;
    font-weight: 400;
  }
  .wine-glass {
    position: absolute;
    left: 628px;
    top: 159px;
    width: 308px;
    height: 925px;
  }
  .footer-band {
    position: absolute;
    left: 0;
    bottom: 0;
    width: 100%;
    height: 66px;
    background: var(--band);
    display: flex;
    align-items: center;
    justify-content: center;
  }
  .contact-email {
    font-size: 15px;
    letter-spacing: 7px;
    color: var(--text);
  }
</style>
</head>
<body>
<main class="profile-page">
  <svg class="facet-lines" width="936" height="1200" viewBox="0 0 936 1200" aria-hidden="true">
    <g fill="none" stroke="rgba(255,160,170,0.12)" stroke-width="1">
      <polyline points="80,420 620,200 830,560 470,1120"/>
      <polyline points="150,900 470,1120 936,760"/>
      <polyline points="620,200 380,640 150,900"/>
      <polyline points="380,640 830,560"/>
    </g>
  </svg>

  <div class="content-frame"></div>

  <header class="brand">
    <div class="brand-dot"></div>
    <span class="brand-name">Valtrenor</span>
  </header>

  <p class="company-text">Valtrenor brings rare, exceptional wines to the Indonesian market. We specialize in French and Italian wines that even in Europe are very hard to get by. We have an extensive network of big and small, famous and less known winemakers that reserve a portion of their production for us. Together with them, we supply the market with an excellent range of the absolute best European wines. We buy our products directly at the winemaker in France or Italy Through a licensed importer, the wines are brought to Indonesia by airfreight and stored in air-conditioned, optimal conditions, awaiting distribution to our customers. All of this ensured that the wine loses none of its quality during transport from the winemaker to the customer. We always look out for partners that are eager to distribute or retail. Our intentions working with them are always to work on a long term basis. With these intentions we see that both sides together have to engage themselves to succeed in sales and establishing brand recognition in the Indonesian market. Our philosophy is based on trust, responsibility, mutual respect and of course a love for great wine! We advise our clients on tasting, food pairing, storing and aging the wine -and provide a technical datasheet with all our bottles. We pride ourselves in our customer service and are always available for any enquiry.</p>

  <svg class="wine-glass" role="img" aria-label="Illustration of a large glass of red wine with a stylised leaf pattern on the glass" width="308" height="925" viewBox="0 0 308 925">
    <defs>
      <linearGradient id="glassTone" x1="0" y1="0" x2="0" y2="1">
        <stop offset="0" stop-color="var(--glass-light)" stop-opacity="0.35"/>
        <stop offset="0.34" stop-color="var(--glass-light)" stop-opacity="0.3"/>
        <stop offset="0.35" stop-color="var(--glass-wine)" stop-opacity="0.9"/>
        <stop offset="0.55" stop-color="var(--glass-wine)" stop-opacity="0.75"/>
        <stop offset="0.56" stop-color="var(--glass-light)" stop-opacity="0.18"/>
        <stop offset="1" stop-color="var(--glass-light)" stop-opacity="0.25"/>
      </linearGradient>
    </defs>
    <rect x="0" y="0" width="308" height="925" fill="url(#glassTone)"/>
  </svg>

  <footer class="footer-band">
    <span class="contact-email">info@valtrenor-example.eu</span>
  </footer>
</main>
</body>
</html>
```